Corporate Brightfen business cards to be handed to investor, bankers etc. Needs to have a young feel

I need business cards designed for a technology company that provides uber-like rapid response on the security industry. I would like it simple but very cool and tasteful. See attached documents for artwork and colours to be used. Cut sheet describes business model. Card stock should be thicker than normal. I would like the one side to be just the art and the other to have the contact info with maybe the pin somewhere.

Target Market(s)

Investors

Industry/Entity Type

Business

Contact Information for Business Card

Would like the logo attached on one side with name address and other info on the other side.

Font styles to use
Other font styles liked:
• See existing logo

Colors
6b449b
886aae
e4daeb
ffffff

Requirements
Must have
• Name: Dorian Felkatsis
• Address: 47 Larkfield Avenue, Toronto, On, M6K2B7
• Tel: 416-7291846
• Email: rolo@brightfen.io
Nice to have
• See logo colours

```html
<!DOCTYPE html>
<html lang="en">
<head>
<meta charset="utf-8">
<title>Brightfen Business Card</title>
<link rel="stylesheet" href="https://fonts.googleapis.com/css2?family=Noticia+Text:wght@400;700&display=swap">
<style>
  :root {
    --brand-purple: #6b449b;
    --brand-violet: #886aae;
    --brand-lilac: #e4daeb;
    --brand-white: #ffffff;
    --icon-ink: #2f2840;
    --edge-shade: #231733;
    --stage: #e3e9ec;
    --pattern-glow: #8f86d6;
  }
  * { margin: 0; padding: 0; box-sizing: border-box; }
  html, body {
    width: 1200px;
    height: 1000px;
    overflow: hidden;
    background: var(--stage);
    font-family: "Noticia Text", Georgia, serif;
  }
  .canvas { position: relative; width: 1200px; height: 1000px; }
  .card {
    position: absolute;
    left: 252px;
    width: 745px;
    height: 418px;
    overflow: hidden;
  }
  .card--front { top: 28px; background: var(--brand-purple); }
  .card--back { top: 557px; }

  .front__pattern {
    position: absolute;
    right: 0;
    top: 0;
    width: 370px;
    height: 418px;
    background:
      radial-gradient(ellipse at 60% 45%, rgba(143,134,214,0.55), rgba(107,68,155,0) 70%),
      linear-gradient(90deg, rgba(107,68,155,0) 0%, rgba(136,106,174,0.5) 40%, rgba(143,134,214,0.45) 100%);
  }
  .front__logo {
    position: absolute;
    left: 33px;
    top: 176px;
    display: flex;
    align-items: center;
    gap: 12px;
  }
  .logo__dot {
    width: 34px;
    height: 34px;
    border-radius: 50%;
    background: var(--brand-violet);
  }
  .logo__name {
    color: var(--brand-white);
    font-weight: 400;
    font-size: 58px;
    line-height: 1;
    letter-spacing: 0.5px;
  }

  .back__art { position: absolute; inset: 0; }
  .contact {
    position: absolute;
    left: 18px;
    top: 100px;
    list-style: none;
    color: var(--brand-white);
    font-size: 20px;
  }
  .contact__item {
    display: flex;
    align-items: center;
    gap: 6px;
    height: 38px;
  }
  .contact__icon { width: 34px; height: 34px; flex: none; fill: var(--icon-ink); }
</style>
</head>
<body>
<main class="canvas">
  <section class="card card--front">
    <div class="front__pattern" role="img" aria-label="Glowing hexagonal circuit network with padlock icons"></div>
    <div class="front__logo">
      <span class="logo__dot"></span>
      <span class="logo__name">brightfen</span>
    </div>
  </section>

  <section class="card card--back">
    <svg class="back__art" width="745" height="418" viewBox="0 0 745 418">
      <rect width="745" height="418" fill="var(--brand-purple)"/>
      <polygon points="572,0 595,0 320,300 450,150" fill="var(--edge-shade)"/>
      <polygon points="595,0 745,0 745,418 243,418" fill="var(--brand-lilac)"/>
    </svg>
    <ul class="contact">
      <li class="contact__item">
        <svg class="contact__icon" viewBox="0 0 34 34"><circle cx="17" cy="10" r="7"/><path d="M3 33 C3 22 9 19 17 19 C25 19 31 22 31 33 Z"/></svg>
        <span>Dorian Felkatsis</span>
      </li>
      <li class="contact__item">
        <svg class="contact__icon" viewBox="0 0 34 34"><path d="M17 2 C10 2 6 7 6 13 C6 21 17 32 17 32 C17 32 28 21 28 13 C28 7 24 2 17 2 Z M17 8 A5 5 0 1 1 16.9 8 Z" fill-rule="evenodd"/></svg>
        <span>47 Larkfield Avenue, Toronto, On, M6K2B7</span>
      </li>
      <li class="contact__item">
        <svg class="contact__icon" viewBox="0 0 34 34"><path d="M8 3 L13 3 L15 10 L11 13 C13 18 16 21 21 23 L24 19 L31 21 L31 26 C31 29 28 31 25 31 C14 30 4 20 3 9 C3 6 5 3 8 3 Z"/></svg>
        <span>416-7291846</span>
      </li>
      <li class="contact__item">
        <svg class="contact__icon" viewBox="0 0 34 34"><path d="M3 8 H31 V27 H3 Z M5 10 L17 19 L29 10" fill="var(--icon-ink)" stroke="var(--brand-purple)" stroke-width="2"/></svg>
        <span>rolo@brightfen.io</span>
      </li>
    </ul>
  </section>
</main>
</body>
</html>
```